Digital Medical Care Start-up: New Web Design Needed

We are a startup in Boston, USA. Our current website has mostly acceptable content but looks outdated and it is ineffective. Viewers - especially possible investors - are turned off. It may also have too much content - especially the table. Current site Https://CareLoomKits.com

Business: we produce apps for surgeons to give their patients. The apps describe the medical procedure they will have, how to prepare, what to do to speed recovery, and how to interpret any symptoms. One app for each medical procedure - there are over 200.

LIKES
https://www.kestrivamed.com/
https://www.fenworthclinix.com/en/
https://zorandi.com/about/
DISLIKES
https://plax-ora.com/
https://www.tundravita.com/
https://www.grelvin-clinic.net/
https://www.quessa.com/

Target Market(s)

Audience: Medical Surgeons (customers) and Investors (we will do our first capital raise afterward the new website) in USA.

Coding

Number of Pages Required

Font styles to use
Other font styles liked:
• Candara

Colors
0455a3
f37122

Requirements
Must have
• OUTPUT:
We want a fully Responsive Version.
We do not use Wordpress. The page layout (or template) should be html + css + images + a little JavaScript.
The first page is the landing page. The second page would be the template on which we put the remaining content.
After delivery, the html would be merged into the existing framework. The site needs to be built on a template so it can be managed by an average quasi-tech person, without the need for a coder.

See exisiting company and product logos. They will remain unchanged, so make sure the website is compatable with the current logos.
Nice to have
• We have attached an idea of ours. This is meant for your stimulation, not necessarily for replication. Our attachment does not have all the content details, but the outline is correct.

```html
<!DOCTYPE html>
<html lang="en">
<head>
<meta charset="utf-8">
<title>CareLoomKits – Digitally Delivering Procedure eCare</title>
<link rel="stylesheet" href="https://fonts.googleapis.com/css2?family=Poppins:wght@400;500;600;700&family=Roboto+Condensed:wght@400;700&display=swap">
<style>
:root{
  --blue:#0455a3;
  --blue-mid:#1e7fcb;
  --blue-light:#29b8ef;
  --sky:#cfeefb;
  --orange:#f37122;
  --ink:#1d1d1d;
  --grey:#555;
  --white:#fff;
}
*{margin:0;padding:0;box-sizing:border-box}
html,body{width:1200px;height:3000px;overflow:hidden;background:#fff}
body{font-family:"Poppins",sans-serif;color:var(--ink);position:relative}
.abs{position:absolute}
.section{position:absolute;left:0;width:1200px;overflow:hidden}

/* header */
.site-header{top:0;height:50px;background:#fff}
.brand{left:86px;top:11px;display:flex;align-items:center;gap:8px;font-size:21px;font-weight:500;color:var(--blue)}
.brand-dot{width:28px;height:28px;border-radius:50%;background:var(--blue-mid)}
.nav{left:0;top:17px;font-size:14px;color:var(--ink)}
.nav span{position:absolute;white-space:nowrap}
.btn{background:var(--orange);color:#fff;border-radius:20px;font-size:12px;display:flex;align-items:center;justify-content:center;font-weight:500;letter-spacing:.3px}
.btn-contact{left:1048px;top:10px;width:110px;height:30px}

/* hero */
.hero{top:50px;height:460px}
.hero-photo{left:0;top:0;width:1200px;height:460px;background:linear-gradient(120deg,#1a8fd0 0%,#1673bd 45%,#0f5aa8 100%)}
.hero-kicker{left:0;width:1200px;top:108px;text-align:center;font-family:"Roboto Condensed",sans-serif;color:#fff;font-size:32px;line-height:40px}
.hero-rule{top:152px;height:3px;background:#fff}
.hero-title{left:0;width:1200px;top:158px;text-align:center;font-family:"Roboto Condensed",sans-serif;font-weight:700;color:#fff;font-size:62px;line-height:74px;letter-spacing:.5px}
.hero-copy{left:230px;width:740px;top:242px;text-align:center;color:#fff;font-size:13px;line-height:21px}
.btn-learn{left:522px;top:302px;width:156px;height:36px;font-size:13px;gap:14px;padding-left:8px}
.btn-learn i{width:26px;height:26px;border-radius:50%;background:#fff;display:flex;align-items:center;justify-content:center}

/* enable */
.enable{top:500px;height:540px}
.enable h2{left:107px;top:45px;font-size:27px;line-height:35px;font-weight:600;letter-spacing:.2px}
.card{background:#fff;box-shadow:0 3px 14px rgba(0,0,0,.13);border-radius:4px;text-align:center}
.feature-card{width:186px;height:152px;padding:16px 12px}
.feature-card svg{display:block;margin:0 auto 10px}
.feature-card h3{font-size:11px;font-weight:600;margin-bottom:6px;line-height:13px}
.feature-card p{font-size:9.5px;line-height:14px;color:var(--grey)}
.team-art{left:600px;top:145px;width:528px;height:345px;border-radius:48% 40% 30% 46%;background:linear-gradient(160deg,#bfeafa,#9fdff5)}

/* features */
.features{top:1020px;height:561px}
.features-bg{left:0;top:0}
.dots{left:95px;top:120px;width:90px;height:90px;background-image:radial-gradient(circle,#0a3f8f 2.4px,transparent 2.6px);background-size:14px 14px}
.doctors-photo{left:45px;top:155px;width:430px;height:430px;border-radius:50%;background:radial-gradient(circle at 50% 40%,#f4f6f8,#dfe5ea)}
.features-title{left:502px;top:100px;width:600px;color:#fff;font-size:28px;font-weight:600;line-height:34px}
.benefit{left:545px;width:610px}
.benefit::before{content:"";position:absolute;left:-32px;top:8px;width:14px;height:14px;border-radius:50%;background:#fff}
.benefit h3{color:#fff;font-size:18px;font-weight:500;line-height:26px}
.benefit p{color:#e6f3fb;font-size:11px;line-height:14px}

/* testimonials */
.testimonials{top:1581px;height:540px;background:linear-gradient(90deg,#cfe0f0 0%,#d5ecf8 50%,#cbeffc 100%)}
.section-title{left:0;width:1200px;text-align:center;font-family:"Roboto Condensed",sans-serif;font-weight:700;font-size:44px;color:#333}
.quote-card{width:412px;height:164px;text-align:left;padding:28px 36px 0}
.quote-card .qm{font-family:"Roboto Condensed",sans-serif;font-size:60px;color:#e7d3b5;line-height:40px;position:absolute;left:44px;top:20px}
.quote-card p{font-size:12px;line-height:18px;color:#333;text-indent:60px}
.quote-tail{width:0;height:0;border-left:40px solid transparent;border-right:20px solid transparent;border-top:26px solid #fff}
.arrow{font-size:34px;color:#333;line-height:20px}
.reviewer{display:flex;align-items:center;gap:12px}
.avatar{width:64px;height:64px;border-radius:50%;background:linear-gradient(160deg,#f0e0d0,#b89478)}
.reviewer b{display:block;font-size:14px;font-weight:600}
.reviewer small{display:block;font-size:12px;color:#444}
.stars{color:#f4c41a;font-size:11px;letter-spacing:2px}

/* clinical */
.clinical{top:2121px;height:535px}
.group-card{text-align:left;padding:0 26px}
.group-art{margin:26px auto 20px;border-radius:6px}
.group-card h3{font-size:15px;font-weight:600;margin-bottom:6px}
.group-card p{font-size:12.5px;line-height:19px;color:#333}
.btn-more{left:912px;top:477px;width:123px;height:36px;font-size:14px}

/* footer */
.site-footer{top:2656px;height:344px}
.footer-brand{left:86px;top:130px;display:flex;align-items:center;gap:12px;color:#fff;font-size:31px;font-weight:500}
.footer-brand .brand-dot{width:44px;height:44px;background:#fff;opacity:.9}
.footer-about{left:86px;top:186px;width:310px;color:#e8f4fb;font-size:11.5px;line-height:15px}
.footer-head{color:#fff;font-size:23px;font-weight:400;top:130px}
.footer-links{left:447px;top:172px;color:#fff;font-size:14px;line-height:21px;list-style:none}
.contact-list{left:667px;top:172px;color:#fff;font-size:15px;list-style:none}
.contact-list li{display:flex;gap:18px;margin-bottom:16px;line-height:20px}
.social{left:942px;top:177px;display:flex;gap:18px}
.social span{width:16px;height:16px;border-radius:50%;background:#fff}
.footer-rule{left:175px;top:308px;width:833px;height:1px;background:#fff}
.copyright{left:0;width:1200px;top:319px;text-align:center;color:#fff;font-size:12.5px}
</style>
</head>
<body>

<header class="section site-header">
  <div class="abs brand"><span class="brand-dot"></span>CareLoomKits</div>
  <nav class="abs nav">
    <span style="left:398px">About Us</span>
    <span style="left:511px">Medical Advisory Board</span>
    <span style="left:731px">Clinical Groups</span>
    <span style="left:893px">Testimonials</span>
  </nav>
  <a class="abs btn btn-contact">CONTACT</a>
</header>

<section class="section hero">
  <div class="abs hero-photo" role="img" aria-label="Photo of surgeons in an operating room, tinted blue"></div>
  <div class="abs hero-kicker">DIGITALLY DELIVERING</div>
  <div class="abs hero-rule" style="left:470px;width:162px"></div>
  <div class="abs hero-rule" style="left:640px;width:52px"></div>
  <h1 class="abs hero-title">PROCEDURE ECARE</h1>
  <p class="abs hero-copy">Lorem Ipsum Dolor Sit Amet, Consectetur Adipiscing Elit. Mauris Neque Gravida Purus Ipsum Phasellus Aliquam At Risus Arcu. Bibendum Quis Sed Ac Non Vitae Varius Interdum Ut Et.</p>
  <a class="abs btn btn-learn">LEARN MORE <i><svg width="14" height="12" viewBox="0 0 14 12"><path d="M2 1l5 5-5 5M7 1l5 5-5 5" fill="none" stroke="#f37122" stroke-width="2"/></svg></i></a>
  <svg class="abs" style="left:0;top:350px" width="1200" height="110" viewBox="0 0 1200 110">
    <path d="M0 75 C120 45 220 10 360 25 C520 45 620 80 780 92 C960 106 1080 82 1200 52 L1200 110 L0 110Z" fill="#fff"/>
    <path d="M0 75 C120 45 220 10 360 25" fill="none" stroke="#1aa6e6" stroke-width="6"/>
  </svg>
</section>

<section class="section enable">
  <h2 class="abs">WE ENABLE CLINICIANS TO INCREASE THE<br>NUMBER OF PROCEDURES – WHILE IMPROVING<br>HEALTH OUTCOMES</h2>
  <svg class="abs" style="left:100px;top:200px" width="430" height="340" viewBox="0 0 430 340">
    <path d="M195 80 H225" stroke="#7aa8dd" stroke-dasharray="8 6" fill="none"/>
    <path d="M195 105 H225" stroke="#7aa8dd" stroke-dasharray="8 6" fill="none"/>
    <path d="M50 140 C55 210 90 255 125 270" stroke="#7aa8dd" stroke-dasharray="8 6" fill="none"/>
    <path d="M78 140 C82 195 105 235 125 245" stroke="#7aa8dd" stroke-dasharray="8 6" fill="none"/>
    <path d="M395 140 C390 210 355 255 310 270" stroke="#7aa8dd" stroke-dasharray="8 6" fill="none"/>
    <path d="M370 140 C365 195 345 235 310 245" stroke="#7aa8dd" stroke-dasharray="8 6" fill="none"/>
  </svg>
  <div class="abs card feature-card" style="left:105px;top:169px">
    <svg width="48" height="40" viewBox="0 0 48 40" fill="none" stroke="#222" stroke-width="1.6"><rect x="4" y="8" width="40" height="8" rx="2"/><circle cx="12" cy="6" r="4"/><path d="M10 16l26 16M38 16L12 32"/><circle cx="10" cy="35" r="3"/><circle cx="38" cy="35" r="3"/></svg>
    <h3>PERIOP TASK</h3>
    <p>Lorem ipsum dolor sit amet, consectetur adipiscing elit. Blandit tellus. adipis ahincing adipiscing elit. Blandit tellus</p>
  </div>
  <div class="abs card feature-card" style="left:322px;top:169px">
    <svg width="48" height="40" viewBox="0 0 48 40" fill="none" stroke="#222" stroke-width="1.6"><rect x="26" y="2" width="16" height="12" rx="2"/><circle cx="34" cy="8" r="3"/><circle cx="15" cy="20" r="5"/><path d="M6 38v-6a9 9 0 0118 0v6"/><circle cx="34" cy="24" r="4"/><path d="M27 38v-5a7 7 0 0114 0v5"/></svg>
    <h3>COMMUNICATION</h3>
    <p>Lorem ipsum dolor sit amet, consectetur adipiscing elit. Blandit tellus. adipis ahincing adipiscing elit. Blandit tellus</p>
  </div>
  <div class="abs card feature-card" style="left:224px;top:340px;height:170px">
    <svg width="40" height="40" viewBox="0 0 40 40" fill="none" stroke="#222" stroke-width="1.6"><circle cx="20" cy="13" r="8"/><path d="M6 38v-6a14 14 0 0128 0v6"/><path d="M14 28v6h12v-6"/></svg>
    <h3>INTERACTIVE<br>SYMPTOMS TRIAGE</h3>
    <p>Lorem ipsum dolor sit amet, consectetur adipiscing elit. Blandit tellus. adipis ahincing adipiscing elit. Blandit tellus</p>
  </div>
  <div class="abs team-art" role="img" aria-label="Illustration of three clinicians in white coats beside a potted plant"></div>
</section>

<section class="section features">
  <svg class="abs features-bg" width="1200" height="561" viewBox="0 0 1200 561">
    <defs>
      <linearGradient id="featGrad" x1="0" y1="0" x2="1" y2="0.3">
        <stop offset="0" stop-color="#1fb6f4"/><stop offset="0.45" stop-color="#1d8fd6"/><stop offset="1" stop-color="#2a6fbd"/>
      </linearGradient>
    </defs>
    <path d="M0 75 C90 20 180 15 300 30 C460 55 560 95 760 90 C950 85 1080 45 1200 25 L1200 561 L0 561Z" fill="url(#featGrad)"/>
    <path d="M0 340 C40 300 110 310 140 380 C180 470 250 520 320 561 L0 561Z" fill="#24c3f8" opacity=".7"/>
  </svg>
  <div class="abs dots"></div>
  <div class="abs doctors-photo" role="img" aria-label="Photo of three smiling doctors in a circular frame"></div>
  <h2 class="abs features-title">We Have The Best Ecare Solution For<br>Surgeries And Treatment</h2>
  <div class="abs benefit" style="top:190px"><h3>Immediate And Measurable Benefits</h3><p>Lorem Ipsum Dolor Sit Amet, Consectetur Adipiscing Elit. Mauris Neque Gravida Purus Ipsum Phasellus Aliquam At Risus Arcu. Bibendum Quis Sed Ac Non Vitae Varius Interdum Ut Et.</p></div>
  <div class="abs benefit" style="top:253px"><h3>Improvement In The Entire Patient Journey</h3><p>Lorem Ipsum Dolor Sit Amet, Consectetur Adipiscing Elit. Mauris Neque Gravida Purus Ipsum Phasellus Aliquam At Risus Arcu. Bibendum Quis Sed Ac Non Vitae Varius Interdum Ut Et.</p></div>
  <div class="abs benefit" style="top:315px"><h3>Provider Specific</h3><p>Lorem Ipsum Dolor Sit Amet, Consectetur Adipiscing Elit. Mauris Neque Gravida Purus Ipsum Phasellus Aliquam At Risus Arcu. Bibendum Quis Sed Ac Non Vitae Varius Interdum Ut Et.</p></div>
  <div class="abs benefit" style="top:379px"><h3>Accessible From Any Device</h3><p>Lorem Ipsum Dolor Sit Amet, Consectetur Adipiscing Elit. Mauris Neque Gravida Purus Ipsum Phasellus Aliquam At Risus Arcu. Bibendum Quis Sed Ac Non Vitae Varius Interdum Ut Et.</p></div>
  <div class="abs benefit" style="top:444px"><h3>No User Manual Needed</h3><p>Lorem Ipsum Dolor Sit Amet, Consectetur Adipiscing Elit. Mauris Neque Gravida Purus Ipsum Phasellus Aliquam At Risus Arcu. Bibendum Quis Sed Ac Non Vitae Varius Interdum Ut Et.</p></div>
</section>

<section class="section testimonials">
  <h2 class="abs section-title" style="top:60px">OUR TESTIMONIAL</h2>
  <span class="abs arrow" style="left:100px;top:226px">⟵</span>
  <span class="abs arrow" style="left:1080px;top:226px">⟶</span>

  <div class="abs card quote-card" style="left:175px;top:154px"><span class="qm">“</span><p>Lorem Ipsum Dolor Sit Amet, Consectetur Adipiscing Odio Ultrices Amet, Congue Integer Any Nibh. Amet, Eget Tristique Vitae A Sed Venenatis. Dictumst Eros Id Vitae Orci Id. Senectus Senectus Parturient Any Time Diam, Namtristique Vitae A Sed Venenatis. Dictumst Dictumst Dictumst Eros Id</p></div>
  <div class="abs quote-tail" style="left:222px;top:318px"></div>
  <div class="abs reviewer" style="left:170px;top:345px"><span class="avatar" role="img" aria-label="Reviewer portrait"></span><div><b>Lorem Ipsum</b><small>Lorem Ipsum</small><span class="stars">★★★★★</span></div></div>

  <div class="abs card quote-card" style="left:614px;top:154px"><span class="qm">“</span><p>Lorem Ipsum Dolor Sit Amet, Consectetur Adipiscing Odio Ultrices Amet, Congue Integer Any Nibh. Amet, Eget Tristique Vitae A Sed Venenatis. Dictumst Eros Id Vitae Orci Id. Senectus Senectus Parturient Any Time Diam, Namtristique Vitae A Sed Venenatis. Dictumst Dictumst Dictumst Eros Id</p></div>
  <div class="abs quote-tail" style="left:661px;top:318px"></div>
  <div class="abs reviewer" style="left:612px;top:345px"><span class="avatar" role="img" aria-label="Reviewer portrait"></span><div><b>Lorem Ipsum</b><small>Lorem Ipsum</small><span class="stars">★★★★★</span></div></div>

  <svg class="abs" style="left:0;top:420px" width="1200" height="120" viewBox="0 0 1200 120">
    <path d="M0 80 C150 30 300 25 470 55 C640 85 760 115 940 105 C1060 98 1140 70 1200 35 L1200 120 L0 120Z" fill="#fff"/>
  </svg>
</section>

<section class="section clinical">
  <h2 class="abs section-title" style="top:60px">OUR CLINICAL GROUPS</h2>
  <div class="abs card group-card" style="left:178px;top:179px;width:243px;height:228px">
    <div class="group-art" role="img" aria-label="Anatomical drawing of the stomach" style="width:110px;height:95px;background:linear-gradient(160deg,#f7c8c8,#e8888f 60%,#7fb4e6)"></div>
    <h3>Bariatric</h3><p>Marlow T. Keene, MD MS FACE Proessor of surgery Westbrook medical school</p>
  </div>
  <div class="abs card group-card" style="left:455px;top:164px;width:259px;height:258px">
    <div class="group-art" role="img" aria-label="Anatomical drawing of the human heart" style="width:110px;height:130px;margin-top:14px;background:linear-gradient(160deg,#e84a3c,#f2b3ad 55%,#6fa3dd)"></div>
    <h3>CARDIAC SURGERY</h3><p>Marlow T. Keene, MD MS FACE Proessor of surgery Westbrook medical school</p>
  </div>
  <div class="abs card group-card" style="left:749px;top:179px;width:242px;height:228px">
    <div class="group-art" role="img" aria-label="Illustration of a hand holding medicine bottles and pills" style="width:140px;height:95px;background:linear-gradient(160deg,#f4d7c0,#d9e4ef 60%,#e0464a)"></div>
    <h3>FERTILITY MEDICINE</h3><p>Marlow T. Keene, MD MS FACE Proessor of surgery Westbrook medical school</p>
  </div>
  <a class="abs btn btn-more">VIEW MORE</a>
</section>

<footer class="section site-footer">
  <svg class="abs" style="left:0;top:0" width="1200" height="344" viewBox="0 0 1200 344">
    <defs>
      <linearGradient id="footGrad" x1="0" y1="0" x2="1" y2="0.4">
        <stop offset="0" stop-color="#22b3e8"/><stop offset="1" stop-color="#2b68b2"/>
      </linearGradient>
    </defs>
    <path d="M0 65 C120 20 260 0 420 25 C600 55 720 80 900 65 C1040 52 1130 35 1200 20 L1200 344 L0 344Z" fill="url(#footGrad)"/>
  </svg>
  <div class="abs footer-brand"><span class="brand-dot"></span>CareLoomKits</div>
  <p class="abs footer-about">Lorem Ipsum Dolor Sit Amet, Consectetur Adipiscing Elit. Mauris Neque Gravida Purus Ipsum Phasellus Aliquam At Risus Arcu. Bibendum</p>

  <h4 class="abs footer-head" style="left:443px">QUICK LINKS</h4>
  <ul class="abs footer-links"><li>Home</li><li>About Us</li><li>Services</li><li>Blog</li><li>Treatment</li><li>Testimonial</li></ul>

  <h4 class="abs footer-head" style="left:667px">CONTACT US</h4>
  <ul class="abs contact-list">
    <li><svg width="22" height="18" viewBox="0 0 24 24"><path d="M6 3l3 4-2 2c1 3 4 6 7 7l2-2 4 3-2 4C10 21 3 14 2 5z" fill="#fff"/></svg>555-0142-86</li>
    <li><svg width="22" height="18" viewBox="0 0 24 24" fill="none" stroke="#fff" stroke-width="1.6"><rect x="3" y="6" width="18" height="12"/><path d="M3 6l9 7 9-7"/></svg>hello@careloomkits.com</li>
    <li><svg width="22" height="18" viewBox="0 0 24 24"><path d="M21 3L3 11l8 2 2 8z" fill="#fff"/></svg>Street no 4 near Elm Square,<br>Brookfield USA</li>
  </ul>

  <h4 class="abs footer-head" style="left:942px">FOLLOW US</h4>
  <div class="abs social"><span></span><span></span><span></span><span></span></div>

  <div class="abs footer-rule"></div>
  <p class="abs copyright">©2021 CARELOOM INC, CARELOOMKITS INC ARE TRADMATE OF CARELOOMKITS INC.</p>
</footer>

</body>
</html>
```